Dietary supplement package design

We need a design for a range of dietary supplements mentioned below. The colors can be derived from the attached company logo and the package is a plastic bottle for medicines use (attached is a sample). All products will have the same package design and color with a permissible slight change to product name and associated picture/artwork (if any). Please avoid using pictures of humans or animals. We expect to see a label with three panels:
1. Left panel containing instructions, warnings and other information.
2. Front panel containing products name and its unique look
3. Right panel containing nutrient/ingredient information table and address.
The label will dual language (Arabic/English) and we have no issue to use special colors, i.e. UV, gold or silver.
Products names are:
1. Ginkgo biloba
2. Slimming formula
3. Fat Absorber
4. Glutathione
5. Royal Jelly
6. Vitamin D
Reason: Allow designers to provide more suggestions
Target Market(s)
Consumers and health care professionals
Industry/Entity Type
Healthcare
Look and feel

```html
<!DOCTYPE html>
<html lang="en">
<head>
<meta charset="utf-8">
<title>Supplement Label Range</title>
<link href="https://fonts.googleapis.com/css2?family=Oswald:wght@500&family=Open+Sans:wght@400;600;700&display=swap" rel="stylesheet">
<style>
  :root {
    --page: #ffffff;
    --ink: #222222;
    --green: #2f9a35;
    --green-tint: #e6f3e4;
    --blue: #3aa6dc;
    --blue-tint: #dfeef7;
    --navy: #17207a;
    --navy-tint: #e6e7f2;
    --brand-blue: #2f8fd0;
    --white: #ffffff;
  }
  * { box-sizing: border-box; margin: 0; padding: 0; }
  html, body { width: 1200px; height: 1200px; overflow: hidden; background: var(--page); }
  body { font-family: "Open Sans", sans-serif; color: var(--ink); }

  .range {
    position: absolute; left: 30px; top: 330px;
    display: flex; gap: 20px;
  }
  .label {
    --accent: var(--green);
    --tint: var(--green-tint);
    width: 366px; height: 540px;
    background: linear-gradient(180deg, var(--white) 0%, var(--tint) 45%, var(--white) 100%);
    border-top: 7px solid var(--accent);
    border-bottom: 7px solid var(--accent);
    display: flex; flex-direction: column; align-items: center;
    padding: 30px 8px 0;
    overflow: hidden;
  }
  .label--blue { --accent: var(--blue); --tint: var(--blue-tint); }
  .label--navy { --accent: var(--navy); --tint: var(--navy-tint); }

  .brand { display: flex; align-items: center; gap: 10px; margin-top: 10px; }
  .brand-mark { width: 34px; height: 34px; background: var(--navy); }
  .brand-name { font-weight: 700; font-size: 34px; color: var(--brand-blue); letter-spacing: -0.5px; }

  .product-name {
    font-family: "Oswald", sans-serif; font-weight: 500;
    font-size: 54px; line-height: 64px; height: 64px; text-transform: uppercase;
    color: var(--accent); margin-top: 34px; white-space: nowrap;
    letter-spacing: -0.5px;
  }
  .label--blue .product-name { font-size: 46px; }
  .label--navy .product-name { font-size: 58px; }

  .blurb {
    font-size: 10.5px; line-height: 15px; text-align: center;
    width: 340px; margin-top: 12px; color: #333;
  }
  .claims {
    margin-top: 22px; width: 320px;
    background: var(--accent); color: var(--white);
    border-radius: 8px 8px 0 0;
    padding: 10px 8px 0; text-align: center;
    font-weight: 600; font-size: 15px; line-height: 1;
  }
  .claims p { padding: 6px 0 8px; white-space: nowrap; }
  .claims p + p { border-top: 1px solid rgba(255,255,255,0.5); }
  .count {
    margin: 4px auto 0; width: 240px;
    background: var(--white); color: var(--ink);
    border-radius: 6px 6px 0 0;
    font-weight: 700; font-size: 19px; padding: 6px 0 8px;
  }
  .label--blue .count { color: var(--blue); }
</style>
</head>
<body>
  <main class="range">
    <section class="label label--green">
      <div class="brand"><span class="brand-mark"></span><span class="brand-name">Veralis Health</span></div>
      <h2 class="product-name">Ginkgo Biloba</h2>
      <p class="blurb">Lorem ipsum dolor sit amet, consectetur adipisicing elit, sed do eiusmod tempor incididunt ut labore et dolore magna aliqua. Ut enim ad minim veniam, quis nostrud exercitation.</p>
      <div class="claims">
        <p>Lorem Ipsum Dolor Sit Amet</p>
        <p>Consectetur Adipisicing Elit Sed Do</p>
        <p>Incididunt Ut Labore et Dolore Magna</p>
        <div class="count">30 Capsules</div>
      </div>
    </section>

    <section class="label label--blue">
      <div class="brand"><span class="brand-mark"></span><span class="brand-name">Veralis Health</span></div>
      <h2 class="product-name">Slimming Formula</h2>
      <p class="blurb">Lorem ipsum dolor sit amet, consectetur adipisicing elit, sed do eiusmod tempor incididunt ut labore et dolore magna aliqua. Ut enim ad minim veniam, quis nostrud exercitation.</p>
      <div class="claims">
        <p>Lorem Ipsum Dolor Sit Amet</p>
        <p>Consectetur Adipisicing Elit Sed Do</p>
        <p>Incididunt Ut Labore et Dolore Magna</p>
        <div class="count">30 Capsules</div>
      </div>
    </section>

    <section class="label label--navy">
      <div class="brand"><span class="brand-mark"></span><span class="brand-name">Veralis Health</span></div>
      <h2 class="product-name">Fat Absorber</h2>
      <p class="blurb">Lorem ipsum dolor sit amet, consectetur adipisicing elit, sed do eiusmod tempor incididunt ut labore et dolore magna aliqua. Ut enim ad minim veniam, quis nostrud exercitation.</p>
      <div class="claims">
        <p>Lorem Ipsum Dolor Sit Amet</p>
        <p>Consectetur Adipisicing Elit Sed Do</p>
        <p>Incididunt Ut Labore et Dolore Magna</p>
        <div class="count">30 Capsules</div>
      </div>
    </section>
  </main>
</body>
</html>
```